How to Implement an Investment Portfolio Even Gerald Pimsly would be Proud of

This is for a workshop at a 55+ Senior community to be held in its clubhouse. We will discuss investing for Growth and Income During Retirement. A postcard will be
mailed through TLQA QRVT so it should meet those requirements sample provided on upload. 6 1/2 inches X 9. Postcard should have eye catching photos, graphics but still be professional looking. Maybe a photo of Gerald Pimsley???

Target Market(s)

Seniors 55+

Industry/Entity Type

Investment

Font styles to use
Serif
Sans Serif

Requirements
Must have
• easy to read with photos
• add Cormoy Hall Front Desk phone number for RSVP (555) 204-3318
Nice to have
• eye catching design

```html
<!DOCTYPE html>
<html lang="en">
<head>
<meta charset="utf-8">
<title>Hollister Financial – Workshop Postcards</title>
<link rel="stylesheet" href="https://fonts.googleapis.com/css2?family=Montserrat:wght@900&family=PT+Sans:ital,wght@0,400;0,700;1,400;1,700&family=PT+Sans+Narrow&display=swap">
<style>
:root{
  --navy:#34388f;
  --navy-text:#2f3592;
  --red:#e3171f;
  --lavender:#cfd0e6;
  --grey-bar:#dcdcde;
  --ink:#1d1d1d;
  --stage:#efe9e1;
  --white:#ffffff;
}
*{margin:0;padding:0;box-sizing:border-box}
html,body{width:1200px;height:832px;overflow:hidden}
body{background:var(--stage);position:relative;font-family:"PT Sans",Arial,sans-serif;color:var(--ink)}
.card{position:absolute;top:60px;width:520px;height:720px;background:var(--white);box-shadow:0 2px 8px rgba(0,0,0,.25);overflow:hidden}
.card--front{left:60px}
.card--back{left:625px}
.abs{position:absolute}
.brand-name{position:absolute;color:var(--navy);font-family:"PT Sans",Arial,sans-serif;font-weight:700;font-size:36px;line-height:1;white-space:nowrap}
.band{position:absolute;left:0;width:520px;background:var(--navy);color:var(--white)}
.photo{position:absolute}

/* front */
.front-photo{left:0;top:85px;width:520px;height:250px;background:linear-gradient(180deg,#e6e6e6 0%,#b9b9b9 40%,#d7d7d7 75%,#f6f6f6 100%)}
.headline{left:38px;top:200px;width:470px;font-family:"Montserrat",Arial,sans-serif;font-weight:900;font-size:27px;line-height:34px;color:var(--navy-text);white-space:nowrap}
.join{left:36px;top:303px;font-weight:700;font-size:21px;color:var(--red)}
.band--time{top:333px;height:28px;font-weight:700;font-size:21px;line-height:28px;padding-left:36px}
.topics-title{left:42px;top:370px;font-weight:700;font-size:19px}
.topics{left:40px;top:398px;width:440px;list-style:none;font-size:15px;line-height:17px}
.topics li{margin-bottom:9px}
.topics li::before{content:"• "}
.bio-band{left:0;top:518px;width:520px;height:106px;background:var(--lavender)}
.bio{left:84px;top:522px;width:262px;font-family:"PT Sans Narrow",Arial,sans-serif;font-size:12.5px;line-height:16px}
.bio-photo{left:353px;top:512px;width:88px;height:120px;background:linear-gradient(180deg,#c9c7c6,#8a8580 55%,#2d2f38);border:1px solid #999}
.refresh{left:0;top:640px;width:520px;text-align:center;font-family:"PT Sans Narrow",Arial,sans-serif;font-weight:700;font-size:14px;color:var(--red)}
.band--rsvp{top:667px;height:53px;text-align:center}
.rsvp-line{display:block;font-weight:700;font-size:20px;line-height:30px;margin-top:2px}
.fineprint{display:block;font-family:"PT Sans Narrow",Arial,sans-serif;font-size:10.5px;line-height:14px}
.icon{display:inline-block;vertical-align:-3px}

/* back */
.back-divider{left:322px;top:16px;width:2px;height:62px;background:var(--navy)}
.contact{left:341px;top:20px;font-size:11.5px;line-height:15px;color:var(--navy);font-style:normal}
.band--topic{top:86px;height:36px;line-height:36px;padding-left:20px;white-space:nowrap}
.band--topic .topic-main{font-size:23px}
.band--topic .topic-sub{font-weight:700;font-size:17px}
.hero{left:10px;top:118px;width:510px;height:224px;background:linear-gradient(100deg,#ffffff 0%,#ffffff 25%,#b8a79b 40%,#d9c2a8 60%,#4d9bd2 85%,#3d8fcf 100%)}
.event{left:32px;top:130px;font-weight:700;font-size:18px;line-height:19px}
.event .free{color:var(--red)}
.event em{font-weight:700}
.band--trust{top:346px;height:30px;line-height:30px;text-align:center;font-weight:700;font-size:20px}
.intro{left:44px;top:382px;font-size:14.5px;line-height:16px;white-space:nowrap}
.intro-strong{left:44px;top:418px;font-weight:700;font-size:14.5px;line-height:16px;color:var(--navy-text);white-space:nowrap}
.check-band{left:0;top:477px;width:520px;height:86px;background:var(--lavender)}
.checklist{left:32px;top:481px;list-style:none;font-style:italic;font-weight:700;font-size:14.5px;line-height:15.5px;color:var(--navy-text)}
.checklist li{display:flex;align-items:center;gap:5px}
.dessert{left:418px;top:470px;width:92px;height:92px;background:linear-gradient(180deg,#d94a52,#f3ece2 55%,#f7f2ea);border-radius:8px}
.treat-note{left:308px;top:494px;width:104px;padding:4px 3px;background:var(--red);border-radius:6px;color:var(--white);font-style:italic;font-weight:700;font-size:9.5px;line-height:12px;text-align:center}
.rsvp-bar{left:0;top:568px;width:520px;height:32px;background:var(--grey-bar);line-height:32px;padding-left:36px;font-weight:700;font-size:15px;color:var(--navy-text)}
.rsvp-bar .red{color:var(--red)}
.address-block{left:127px;top:622px;width:193px;height:80px;border:1px solid #333;font-family:Arial,sans-serif;font-size:12px;padding:16px 0 0 10px;line-height:14px}
.address-block .route{position:absolute;right:8px;top:2px;font-size:9px;letter-spacing:.3px}
.address-block .to{margin-top:12px;display:block}
.indicia{left:324px;top:617px;width:72px;height:60px;border:1px solid #333;font-family:Arial,sans-serif;font-size:8px;line-height:10px;text-align:center;padding-top:4px}
</style>
</head>
<body>

<section class="card card--front" aria-label="Workshop invitation, front">
  <p class="brand-name" style="left:0;width:520px;text-align:center;top:30px">Hollister Financial</p>

  <div class="photo front-photo" role="img" aria-label="Black and white close-up photo of a thoughtful older man wearing glasses"></div>

  <h1 class="abs headline">Who else wants<br>a Better Investment<br>Strategy and Less Stress?</h1>
  <p class="abs join">Join us at</p>
  <div class="band band--time">Cormoy Hall | 6:30 PM to 8 PM</div>

  <h2 class="abs topics-title">At this workshop, Dean will discuss:</h2>
  <ul class="abs topics">
    <li>How to enjoy life to the fullest, without worrying about economic downturns.</li>
    <li>Getting rid of (often hidden) investment cost that drag down investmentresults once and for all</li>
    <li>A simple and easy way to grow and protect your retirement assets for a financially secure retirement.</li>
  </ul>

  <div class="abs bio-band"></div>
  <p class="abs bio">Dean Hollister is a LICENSED RETIREMENT PLANNER, specializing in asset management of IRA, retirement and investment account. Hollister Advisors, LLC is independent of a broker-dealer and has low cost, commission free business model. Concierge level service is provided to Maple Ridge Preserve resident.</p>
  <div class="photo bio-photo" role="img" aria-label="Portrait photo of the planner in a dark suit and tie"></div>

  <p class="abs refresh">Gourmet Deli Sandwiches, Cheesecake, Fruit and refreshments will be proivided.</p>

  <div class="band band--rsvp">
    <span class="rsvp-line">RSVP at Cormoy Hall |
      <svg class="icon" width="18" height="18" viewBox="0 0 20 20" aria-hidden="true"><circle cx="10" cy="10" r="8.5" fill="none" stroke="#fff" stroke-width="1.6"/><path d="M7 5.5l2 2-1 1.3c.6 1.3 1.6 2.3 2.9 2.9l1.3-1 2 2-1.2 1.4c-3.3-.5-6.2-3.4-6.7-6.7z" fill="#fff"/></svg>
      (555) 204-3318</span>
    <span class="fineprint">For more information visit: www.HollisterFinancial.com or call (555) 308.4170 · 418 Larkspur Glen Drive, Fairvale, NC 27000</span>
  </div>
</section>

<section class="card card--back" aria-label="Workshop invitation, mailing side">
  <p class="brand-name" style="left:22px;top:30px">Hollister Financial</p>
  <div class="abs back-divider"></div>
  <address class="abs contact">
    418 Larkspur Glen Drive<br>Fairvale, NC 27000<br>
    <svg class="icon" width="12" height="12" viewBox="0 0 20 20" aria-hidden="true"><circle cx="10" cy="10" r="8.5" fill="none" stroke="#34388f" stroke-width="1.8"/><path d="M7 5.5l2 2-1 1.3c.6 1.3 1.6 2.3 2.9 2.9l1.3-1 2 2-1.2 1.4c-3.3-.5-6.2-3.4-6.7-6.7z" fill="#34388f"/></svg>(555) 308.417<br>
    www.HollisterFinancial.com
  </address>

  <div class="band band--topic"><span class="topic-main">Investing &amp; Retirement</span> <span class="topic-main">|</span> <span class="topic-sub">A focus on growth and Income</span></div>

  <div class="photo hero" role="img" aria-label="A house resting on a pile of banknotes beside a smiling retired couple embracing"></div>
  <p class="abs event">Join us for <span class="free">FREE at Cormoy Hall</span><br><em>Sign-up at front desk</em><br>November 3 | 6:30 to 8:00 PM</p>

  <div class="band band--trust">A LICENSED PLANNER You Can Trust</div>
  <p class="abs intro">Dean Hollister is a licensed retirement planner who specializes<br>in helping Seniors preserve their quality of life during retirement.</p>
  <p class="abs intro-strong">Dean will discuss how to identify and reduce the cost of investing.<br>This may affect your overall return by reducing or eliminating<br>hidden expenses, fees, commissions and taxes.</p>

  <div class="abs check-band"></div>
  <ul class="abs checklist">
    <li><svg width="11" height="11" viewBox="0 0 12 12" aria-hidden="true"><rect x=".5" y=".5" width="11" height="11" fill="#fff" stroke="#2f3592"/><path d="M2.5 6l2.5 2.5 4.5-5.5" fill="none" stroke="#2f3592" stroke-width="1.6"/></svg>Maximizing Income Flow in Retirement</li>
    <li><svg width="11" height="11" viewBox="0 0 12 12" aria-hidden="true"><rect x=".5" y=".5" width="11" height="11" fill="#fff" stroke="#2f3592"/><path d="M2.5 6l2.5 2.5 4.5-5.5" fill="none" stroke="#2f3592" stroke-width="1.6"/></svg>Options to Pay for Long-Term Care</li>
    <li><svg width="11" height="11" viewBox="0 0 12 12" aria-hidden="true"><rect x=".5" y=".5" width="11" height="11" fill="#fff" stroke="#2f3592"/><path d="M2.5 6l2.5 2.5 4.5-5.5" fill="none" stroke="#2f3592" stroke-width="1.6"/></svg>Retirement Investment Strategies</li>
    <li><svg width="11" height="11" viewBox="0 0 12 12" aria-hidden="true"><rect x=".5" y=".5" width="11" height="11" fill="#fff" stroke="#2f3592"/><path d="M2.5 6l2.5 2.5 4.5-5.5" fill="none" stroke="#2f3592" stroke-width="1.6"/></svg>Reducing Investment Costs and Taxes</li>
    <li><svg width="11" height="11" viewBox="0 0 12 12" aria-hidden="true"><rect x=".5" y=".5" width="11" height="11" fill="#fff" stroke="#2f3592"/><path d="M2.5 6l2.5 2.5 4.5-5.5" fill="none" stroke="#2f3592" stroke-width="1.6"/></svg>Estate Conservation Strategies</li>
  </ul>
  <div class="photo dessert" role="img" aria-label="Slice of cheesecake topped with raspberries"></div>
  <p class="abs treat-note">Food &amp; Refreshments will be served, along with trivia &amp; prizes.</p>

  <p class="abs rsvp-bar"><span class="red">RSVP at Cormoy Hall Front Desk</span> or Call
    <svg class="icon" width="14" height="14" viewBox="0 0 20 20" aria-hidden="true"><circle cx="10" cy="10" r="8.5" fill="none" stroke="#2f3592" stroke-width="1.8"/><path d="M7 5.5l2 2-1 1.3c.6 1.3 1.6 2.3 2.9 2.9l1.3-1 2 2-1.2 1.4c-3.3-.5-6.2-3.4-6.7-6.7z" fill="#2f3592"/></svg>(555) 308.417</p>

  <div class="abs address-block">
    <span class="route">*****************ECRWSS****</span>
    <span class="to">Local<br>Postal Customer</span>
  </div>
  <div class="abs indicia">PRSRT STD<br>ECRWSS<br>U.S. Postage<br><strong>PAID</strong><br>TLQA RETAIL</div>
</section>

</body>
</html>
```